Web Design for the following 4/5 pages adopting the guidance set out in slide 3 to 7

Brivo’s ambition is to be the leading multi-play challenger offering smart energy, fixed and mobile communication services to consumers. We are now looking for a professional design of our pre-launch website as per guidance attached below.

Provide layout in PSD, jpeg, png and PDF.
Provide full code depending on the platform (i.e. Wordpress, HTML/CSS/Bootstrap etc.).
The existing site has text content for each page. We can tweak to meet specific designs if needed. “Leadership Team” and “Careers” could potentially be merged in one page.
Web design to focus on UX to achieve the objectives set out above.
Embrace the five colours used in the logo as well as black and white.
Feel free to adopt any of the above colours for the header an footer

Target Market(s)

Consumer, Domestic Customers

Number of Pages Required

4 page

Requirements
Must have
• Provide layout in PSD, jpeg, png and PDF.
• Web design to focus on UX to achieve the objectives set out in the guidance.
• Embrace the five colours used in the logo as well as black and white.
• Feel free to adopt any of the above colours for the header an footer
Nice to have
• The existing site has text content for each page. We can tweak to meet specific designs if needed. “Leadership Team” and “Careers” could potentially be merged in one page.

```html
<!DOCTYPE html>
<html lang="en">
<head>
<meta charset="utf-8">
<title>Brivo — Pre-launch</title>
<link href="https://fonts.googleapis.com/css2?family=Lato:wght@300;400;700;900&display=swap" rel="stylesheet">
<style>
:root{
  --pink:#e5177e;
  --magenta:#c2187f;
  --orange:#f39a1e;
  --green:#7dc242;
  --blue:#2f8fd8;
  --purple:#8e3fa4;
  --ink:#2b2b36;
  --dark:#2f2f3d;
  --darker:#262631;
  --grey:#f1f1f3;
  --text:#4a4a55;
  --muted:#8a8a96;
  --white:#ffffff;
}
*{box-sizing:border-box;margin:0;padding:0}
html,body{width:1200px;height:4724px;overflow:hidden}
body{font-family:"Lato",Arial,sans-serif;color:var(--text);background:var(--white)}
section,header,footer{position:relative;width:1200px;overflow:hidden}
.wordmark{display:flex;align-items:center;gap:12px;font-weight:900;font-size:36px;color:var(--ink)}
.wordmark-dot{width:32px;height:32px;border-radius:50%;background:var(--pink)}
.wordmark.light{color:var(--white)}

/* Header */
.site-header{height:136px;display:flex;align-items:center;justify-content:space-between;padding:0 88px}
.main-nav{display:flex;gap:34px;font-size:17px;color:var(--ink)}
.main-nav .active{color:var(--pink)}

/* Hero */
.hero{height:484px}
.hero-photo{position:absolute;inset:0;background:linear-gradient(100deg,#6b625a 0%,#8a8177 35%,#5c5b62 65%,#2d3140 100%)}
.hero-content{position:absolute;left:88px;top:232px;color:var(--white)}
.hero-title{font-size:52px;font-weight:400;letter-spacing:2px}
.hero-sub{font-size:19px;margin-top:14px}
.hero-actions{display:flex;gap:20px;margin-top:48px}
.hero-btn{width:120px;height:24px;font-size:11px;display:flex;align-items:center;justify-content:center;color:var(--white)}
.hero-btn.pink{background:var(--pink)}
.hero-btn.green{background:var(--green)}
.hero-dots{position:absolute;left:560px;top:396px;display:flex;gap:12px}
.hero-dots span{width:12px;height:12px;border-radius:50%;background:rgba(255,255,255,.55)}
.hero-dots span:first-child{background:var(--white)}

/* Section headings */
.section-title{text-align:center;font-size:34px;font-weight:400;color:var(--ink);letter-spacing:1px}
.section-sub{text-align:center;font-size:16px;color:var(--text);margin-top:14px}

/* Services */
.services{height:800px;background:linear-gradient(180deg,#f6f6f8 0%,#ececf0 100%);padding-top:78px}
.services-intro{width:780px;margin:22px auto 0;text-align:center;font-size:13px;line-height:1.7;color:var(--text)}
.service-cards{display:flex;justify-content:center;gap:56px;margin-top:120px}
.service-card{position:relative;width:304px;height:290px;background:var(--white);border:4px solid var(--pink);text-align:center;padding-top:98px}
.service-card.energy{border-color:var(--pink)}
.service-card.phone{border-color:var(--green)}
.service-card.mobile{border-color:var(--blue)}
.service-icon{position:absolute;left:50%;top:-92px;transform:translateX(-50%);width:160px;height:160px;border-radius:50%;background:var(--white);border:4px solid currentColor;display:flex;align-items:center;justify-content:center}
.service-icon-inner{width:128px;height:128px;border-radius:50%;background:currentColor;display:flex;align-items:center;justify-content:center}
.energy .service-icon{color:var(--pink)}
.phone .service-icon{color:var(--green)}
.mobile .service-icon{color:var(--blue)}
.service-name{font-size:22px;font-weight:700;color:var(--ink)}
.service-points{list-style:none;font-size:11px;line-height:2.1;margin-top:10px}
.read-more{display:inline-block;margin-top:14px;border:2px solid var(--ink);font-size:11px;padding:4px 20px;color:var(--ink)}

/* Why */
.why{height:750px;background:var(--dark);color:var(--white);padding:86px 0 0 88px}
.why-title{font-size:34px;font-weight:400;letter-spacing:1px}
.why-sub{font-size:14px;margin-top:12px;color:#d8d8de}
.why-list{list-style:none;margin-top:38px}
.why-item{display:flex;gap:26px;margin-bottom:30px}
.why-item svg{flex:none;margin-top:2px}
.why-item h3{font-size:17px;font-weight:400;color:var(--white)}
.why-item p{font-size:11px;color:#a8a8b4;margin-top:6px}
.device-photo{position:absolute;border-radius:48px}
.why .device-photo{left:860px;top:-40px;width:280px;height:540px;background:linear-gradient(180deg,#e9e9ee,#c9c9d2)}

/* App */
.app{height:900px;padding-top:100px}
.app .device-photo{left:232px;top:226px;width:260px;height:540px;background:linear-gradient(180deg,#dfe2ea 0%,#2a5f9e 20%,#1b3f75 100%)}
.app-features{position:absolute;left:648px;top:296px;list-style:none}
.app-features li{display:flex;align-items:center;gap:24px;font-size:16px;color:var(--ink);margin-bottom:42px}
.arrow-badge{width:40px;height:40px;border:3px solid var(--pink);border-radius:50%;display:flex;align-items:center;justify-content:center}

/* Bundles */
.bundles{height:580px;background:var(--grey);padding-top:84px}
.bundles-note{width:560px;margin:20px auto 0;text-align:center;font-size:12px;line-height:1.6}
.bundle-list{display:flex;justify-content:center;gap:150px;margin-top:42px}
.bundle{width:220px;text-align:center;font-size:15px;color:var(--ink)}
.bundle-icon{width:96px;height:96px;border-radius:50%;margin:0 auto 24px;display:flex;align-items:center;justify-content:center}
.bundle-icon.pink{background:linear-gradient(135deg,#f06aa8,var(--pink))}
.bundle-icon.green{background:linear-gradient(135deg,#a9dd7c,var(--green))}
.bundle-icon.blue{background:linear-gradient(135deg,#7cbcf0,var(--blue))}

/* Register */
.register{height:670px;padding-top:90px}
.register-lead{text-align:center;font-size:15px;font-weight:700;color:var(--ink);margin-top:18px;letter-spacing:1px}
.register-text{width:560px;margin:30px auto 0;text-align:center;font-size:14px;line-height:1.7}
.register-form{width:704px;margin:56px auto 0}
.field{display:block;height:56px;border:2px solid #d3b6e6;border-left-color:var(--purple);margin-bottom:34px;padding:0 24px;line-height:52px;font-size:15px;color:var(--muted);background:var(--white)}
.send-btn{display:block;height:76px;line-height:76px;text-align:center;font-size:26px;letter-spacing:2px;color:var(--white);background:linear-gradient(90deg,var(--pink),var(--magenta) 60%,var(--purple))}

/* Footer */
.site-footer{height:404px;background:var(--dark);color:var(--white)}
.footer-main{display:flex;padding:80px 0 0 88px;height:344px}
.footer-brand{width:230px;padding-top:78px}
.footer-col{margin-right:60px}
.footer-col h4{font-size:22px;font-weight:700;margin-bottom:26px}
.contact-row{display:flex;gap:16px;font-size:12px;color:#c8c8d2;margin-bottom:20px;line-height:1.5}
.social{list-style:none;font-size:13px;color:#c8c8d2;line-height:2.1}
.subscribe-text{width:250px;font-size:12px;color:#c8c8d2;line-height:1.5}
.subscribe-form{display:flex;margin-top:20px}
.subscribe-input{width:216px;height:36px;background:var(--white);color:var(--muted);font-size:12px;padding:0 12px;line-height:36px}
.subscribe-btn{width:36px;height:36px;background:var(--pink);display:flex;align-items:center;justify-content:center}
.footer-bar{height:60px;background:var(--darker);display:flex;align-items:center;justify-content:space-between;padding:0 88px 0 460px;font-size:12px;color:#a8a8b4}
</style>
</head>
<body>

<header class="site-header">
  <div class="wordmark"><span class="wordmark-dot"></span>Brivo</div>
  <nav class="main-nav">
    <span class="active">Home</span><span>About Us</span><span>Leadership Team</span><span>Careers</span><span>Contact Us</span>
  </nav>
</header>

<section class="hero">
  <div class="hero-photo" role="img" aria-label="Photo of a hand holding a smartphone showing the Brivo app in a modern living room"></div>
  <div class="hero-content">
    <h1 class="hero-title">INTRODUCING BRIVO</h1>
    <p class="hero-sub">The smart network for your smart home</p>
    <div class="hero-actions">
      <span class="hero-btn pink">Get Started</span>
      <span class="hero-btn green">Learn More</span>
    </div>
  </div>
  <div class="hero-dots"><span></span><span></span><span></span></div>
</section>

<section class="services">
  <h2 class="section-title">SERVICES</h2>
  <p class="services-intro">One provider for the energy, broadband, landline and mobile services your home relies on every day. Simple pricing, fair tariffs and rewards that grow as you add more services to your account.</p>
  <div class="service-cards">
    <article class="service-card energy">
      <div class="service-icon"><div class="service-icon-inner">
        <svg width="54" height="64" viewBox="0 0 54 64"><path d="M32 2 6 36h18l-6 26 30-38H28z" fill="#fff"/></svg>
      </div></div>
      <h3 class="service-name">Energy</h3>
      <ul class="service-points">
        <li>Great value tariffs with up to 5% savings</li>
        <li>Smart Meter switch over</li>
        <li>Earn Brivo Bundle rewards</li>
      </ul>
      <span class="read-more">Read More</span>
    </article>
    <article class="service-card phone">
      <div class="service-icon"><div class="service-icon-inner">
        <svg width="64" height="56" viewBox="0 0 64 56"><path d="M4 18c0-8 12-12 28-12s28 4 28 12v4h-14v-6H18v6H4z" fill="#fff"/><rect x="14" y="26" width="36" height="26" rx="4" fill="#fff"/><circle cx="32" cy="39" r="7" fill="#7dc242"/></svg>
      </div></div>
      <h3 class="service-name">Phone &amp; Fibre</h3>
      <ul class="service-points">
        <li>FREE Broadband</li>
        <li>Unlimited downloads</li>
        <li>Guaranteed savings on</li>
      </ul>
      <span class="read-more">Read More</span>
    </article>
    <article class="service-card mobile">
      <div class="service-icon"><div class="service-icon-inner">
        <svg width="40" height="66" viewBox="0 0 40 66"><rect x="2" y="2" width="36" height="62" rx="6" fill="none" stroke="#fff" stroke-width="4"/><rect x="8" y="10" width="24" height="40" fill="#fff"/><circle cx="20" cy="57" r="3" fill="#fff"/></svg>
      </div></div>
      <h3 class="service-name">Mobile</h3>
      <ul class="service-points">
        <li>Three simple price plans</li>
        <li>Share your data with family members</li>
        <li>Roam for free</li>
      </ul>
      <span class="read-more">Read More</span>
    </article>
  </div>
</section>

<section class="why">
  <h2 class="why-title">WHY BRIVO</h2>
  <p class="why-sub">A few reasons to join Brivo:</p>
  <ul class="why-list">
    <li class="why-item">
      <svg width="26" height="26" viewBox="0 0 26 26"><path d="M13 2l3.4 7 7.6 1-5.5 5.3 1.3 7.7L13 19.4 6.2 23l1.3-7.7L2 10l7.6-1z" fill="none" stroke="#e5177e" stroke-width="2"/></svg>
      <div><h3>Great Value</h3><p>Fair pricing set against the best energy and telecoms tariffs</p></div>
    </li>
    <li class="why-item">
      <svg width="26" height="26" viewBox="0 0 26 26"><rect x="3" y="3" width="20" height="20" rx="3" fill="none" stroke="#e5177e" stroke-width="2"/><path d="M8 13l4 4 7-8" fill="none" stroke="#e5177e" stroke-width="2"/></svg>
      <div><h3>Brivo Bundle</h3><p>Bundle services and get rewards for combining your household bills</p></div>
    </li>
    <li class="why-item">
      <svg width="26" height="26" viewBox="0 0 26 26"><circle cx="13" cy="13" r="10" fill="none" stroke="#e5177e" stroke-width="2"/><path d="M13 7v6l4 3" fill="none" stroke="#e5177e" stroke-width="2"/></svg>
      <div><h3>Control</h3><p>Manage your spend and account online on the go</p></div>
    </li>
    <li class="why-item">
      <svg width="26" height="26" viewBox="0 0 26 26"><rect x="7" y="2" width="12" height="22" rx="2" fill="none" stroke="#e5177e" stroke-width="2"/><circle cx="13" cy="20" r="1.5" fill="#e5177e"/></svg>
      <div><h3>Convenience</h3><p>Access your services any time with one easy to use app</p></div>
    </li>
    <li class="why-item">
      <svg width="26" height="26" viewBox="0 0 26 26"><path d="M13 23s-9-6-9-12a5 5 0 0 1 9-3 5 5 0 0 1 9 3c0 6-9 12-9 12z" fill="none" stroke="#e5177e" stroke-width="2"/></svg>
      <div><h3>Giving</h3><p>Donate some of your spend to the charity of your choice through your Brivo Bundle account each month</p></div>
    </li>
    <li class="why-item">
      <svg width="26" height="26" viewBox="0 0 26 26"><circle cx="13" cy="9" r="5" fill="none" stroke="#e5177e" stroke-width="2"/><path d="M3 24c1-6 5-8 10-8s9 2 10 8" fill="none" stroke="#e5177e" stroke-width="2"/></svg>
      <div><h3>Service</h3><p>A digital first company with friendly support from real local people</p></div>
    </li>
  </ul>
  <div class="device-photo" role="img" aria-label="Photo of a white smartphone displaying the Brivo app splash screen"></div>
</section>

<section class="app">
  <h2 class="section-title">OUR BRIVO APP</h2>
  <p class="section-sub">Manage your every day services with our easy to use Brivo App</p>
  <div class="device-photo" role="img" aria-label="Photo of a white smartphone showing the Brivo app dashboard with usage gauge"></div>
  <ul class="app-features">
    <li><span class="arrow-badge"><svg width="14" height="16" viewBox="0 0 14 16"><path d="M3 2l7 6-7 6" fill="none" stroke="#e5177e" stroke-width="3"/></svg></span>VIEW BILLS</li>
    <li><span class="arrow-badge"><svg width="14" height="16" viewBox="0 0 14 16"><path d="M3 2l7 6-7 6" fill="none" stroke="#e5177e" stroke-width="3"/></svg></span>SWITCH TARIFF</li>
    <li><span class="arrow-badge"><svg width="14" height="16" viewBox="0 0 14 16"><path d="M3 2l7 6-7 6" fill="none" stroke="#e5177e" stroke-width="3"/></svg></span>LOG ISSUES &amp; TRACKS FAULTS</li>
    <li><span class="arrow-badge"><svg width="14" height="16" viewBox="0 0 14 16"><path d="M3 2l7 6-7 6" fill="none" stroke="#e5177e" stroke-width="3"/></svg></span>HELPFUL SPEND AND USAGE ALERTS</li>
    <li><span class="arrow-badge"><svg width="14" height="16" viewBox="0 0 14 16"><path d="M3 2l7 6-7 6" fill="none" stroke="#e5177e" stroke-width="3"/></svg></span>RENEW CONTRACT</li>
  </ul>
</section>

<section class="bundles">
  <h2 class="section-title">BRIVO BUNDLES</h2>
  <p class="section-sub">Benefit from one of our exciting Brivo Bundles</p>
  <p class="bundles-note">To avail of a Brivo Bundle, take two or more services and unlock discounts and giveaways for taking multiple services from Brivo.</p>
  <div class="bundle-list">
    <div class="bundle">
      <div class="bundle-icon pink"><svg width="48" height="40" viewBox="0 0 48 40"><rect x="4" y="20" width="40" height="14" rx="3" fill="#fff"/><path d="M14 20V6M34 20V6" stroke="#fff" stroke-width="3"/></svg></div>
      FREE BROADBAND
    </div>
    <div class="bundle">
      <div class="bundle-icon green"><svg width="40" height="40" viewBox="0 0 40 40"><path d="M10 4l7 8-4 4c2 5 6 9 11 11l4-4 8 7-5 6C17 34 6 23 4 9z" fill="#fff"/></svg></div>
      FREE NATIONAL CALLS FROM YOUR LANDLINE
    </div>
    <div class="bundle">
      <div class="bundle-icon blue"><svg width="44" height="44" viewBox="0 0 44 44"><circle cx="22" cy="22" r="18" fill="none" stroke="#fff" stroke-width="3"/><path d="M28 15c-2-2-10-3-10 2s10 3 10 9-9 5-12 2M22 9v26" fill="none" stroke="#fff" stroke-width="3"/></svg></div>
      ATTRACTIVE CASHBACK OFFERS
    </div>
  </div>
</section>

<section class="register">
  <h2 class="section-title">REGISTER NOW</h2>
  <p class="register-lead">WE ARE LAUNCHING SOON.</p>
  <p class="register-text">Tell us a little about yourself to learn more about the benefits of joining Brivo.<br>For starters, you'll receive a €25 gift card once you sign up to your first Brivo service.</p>
  <div class="register-form">
    <span class="field">First Name</span>
    <span class="field">Phone</span>
    <span class="field">Email</span>
    <span class="send-btn">SEND</span>
  </div>
</section>

<footer class="site-footer">
  <div class="footer-main">
    <div class="footer-brand"><div class="wordmark light"><span class="wordmark-dot"></span>Brivo</div></div>
    <div class="footer-col">
      <h4>Get in touch</h4>
      <div class="contact-row"><svg width="14" height="18" viewBox="0 0 14 18"><path d="M7 1a6 6 0 0 1 6 6c0 4-6 10-6 10S1 11 1 7a6 6 0 0 1 6-6z" fill="#fff"/><circle cx="7" cy="7" r="2" fill="#2f2f3d"/></svg><span>Unit 4, Harbour Court,<br>Northfield, NF2 8QT</span></div>
      <div class="contact-row"><svg width="14" height="14" viewBox="0 0 14 14"><path d="M3 1l3 3-2 2c1 2 2 3 4 4l2-2 3 3-2 2C6 13 1 8 1 3z" fill="#fff"/></svg><span>+00 55 0142 7781</span></div>
      <div class="contact-row"><svg width="16" height="12" viewBox="0 0 16 12"><rect x="1" y="1" width="14" height="10" fill="none" stroke="#fff" stroke-width="1.5"/><path d="M1 1l7 6 7-6" fill="none" stroke="#fff" stroke-width="1.5"/></svg><span>hello@brivo-home.example</span></div>
    </div>
    <div class="footer-col">
      <h4>Follow Us</h4>
      <ul class="social"><li>› Friendsheet</li><li>› Chatterly</li><li>› Worklinker</li><li>› Searchplus</li></ul>
    </div>
    <div class="footer-col">
      <h4>Subscribe</h4>
      <p class="subscribe-text">Leave your email and we will keep you posted on our launch news.</p>
      <div class="subscribe-form">
        <span class="subscribe-input">Enter Your Email</span>
        <span class="subscribe-btn"><svg width="10" height="14" viewBox="0 0 10 14"><path d="M2 1l6 6-6 6" fill="none" stroke="#fff" stroke-width="2.5"/></svg></span>
      </div>
    </div>
  </div>
  <div class="footer-bar"><span>© 2017 Brivo. All Rights Reserved</span><span>Links</span></div>
</footer>

</body>
</html>
```